Redo our website for our Robotics company

We sell robotic equipment to the restaurant industry. Our current robot, is a cooking robot that cooks up to 15 lbs of food. We will provide a prior website as well as brand guidelines. We plan on using wordpress and take advantage of wordpress's visual (no code) editor.

Current website - https://kelvatrix482.com/ (please note we are only selling Pindle now and no longer selling Quado+

We want someone to take our existing content and design the website as well as layout our content we provide. Here's a suggested site layout:

✅ KelvaTrix482 Website Wireframe / Site Map
1. Home

Purpose: Introduce Pindle, establish credibility, drive demo requests.

Sections:

Hero Section

Headline: “Meet Pindle — Your New Robotic Chef for High-Volume, Consistent Cooking.”

Sub-headline: Increase throughput. Reduce labor. Deliver perfect food every time.

CTA: Request a Demo + Watch Pindle Cook

Visual: Video loop or hero animation of Pindle in action.

How Pindle Works (3-4 steps)

Step cards: Load Ingredients → Select Recipe → Pindle Cooks → Serve

Icons and short explanations.

Key Benefits

Labor savings

Zero inconsistency

24/7 uptime

Throughput increases (30–50% faster)

Health & safety compliance

Who It’s For

QSR restaurants

Fast casual

Catering/commissaries

Ghost kitchens

Case Studies / Testimonials

Logo bar + quotes

“Pindle helped us reduce cooking times by 40%.”

Video Section

“Watch Pindle cook a full batch from start to finish.”

CTA Section

Big banner: Book a Demo

2. Product: “Meet Pindle”

Purpose: Deep dive into hardware, software, safety, reliability.

Sections:

Overview

What Pindle is

What tasks it automates

Where it fits in a kitchen

Hardware Features

High-temperature cooking chamber

Precision sensors

Automated stirring

Automated dispensing

Safety mechanisms (locking lids, auto-shutoff)

Software & AI

Recipe automation

IoT dashboard

Remote monitoring

Predictive maintenance

Specs Table

Dimensions

Power requirements

Capacity (lbs per batch)

Safety certifications

Gallery

Close-ups, installation photos, process shots

CTA: Request a Demo

3. Solutions

Purpose: Show that Pindle solves real operational problems.

Sub-pages or sections:

For Quick-Service Restaurants

Reduce labor cost

Speed up peak-hour demand

For Catering & Commissaries

Large-batch consistency

Automate repetitive cooking tasks

For High-Growth Chains

Replicable quality across multiple locations

Centralized recipe control

Each solution page includes:

A problem statement

How Pindle solves it

Metrics / KPIs

Relevant testimonial

CTA

4. ROI / Economics

Purpose: Sell the financial story clearly.

Sections:

Savings Calculator

Labor hours saved

Cost savings

Throughput increases

Food waste reduction

Before & After Comparison

Traditional kitchen vs. robotic kitchen

Sample ROI

“Payback in as little as 3–6 months.”

Download Full ROI Report (PDF)

5. Case Studies

Purpose: Social proof + real results.

Structure for each case study:

Customer background

Problem

Implementation

KPIs achieved

Labor savings

Consistency improvements

Cooking speed

Quote + photos/video

6. Pricing

Purpose: Start a commercial conversation.

Include:

Subscription model (monthly / annual)

Hardware leasing or purchase options

Installation + training

Support level

CTA to book a sales call

7. About

Purpose: Build trust.

Sections:

Mission statement

Founding team

Advisors/partners

“Why we built Pindle”

8. Resources

Purpose: SEO + education.

Subpages:

Blog (e.g., “The Future of Automated Kitchens”)

Whitepapers

Technical documentation

Product videos

9. Contact

General inquiry form

Sales contact

Support portal

Careers

```html
<!DOCTYPE html>
<html lang="en">
<head>
<meta charset="utf-8">
<title>KelvaTrix482 — Meet Pindle</title>
<link href="https://fonts.googleapis.com/css2?family=Roboto:ital,wght@0,400;0,500;0,700;0,900;1,400&display=swap" rel="stylesheet">
<style>
:root{
  --red:#ee1d25;
  --orange:#ff6a3d;
  --cream:#fdeee4;
  --ink:#1d1d1d;
  --grey:#666;
  --nav:#ebebeb;
  --dark:#262626;
  --line:#dcdcdc;
}
*{margin:0;padding:0;box-sizing:border-box}
html,body{width:1200px;height:4367px;overflow:hidden}
body{font-family:"Roboto",Arial,sans-serif;color:var(--ink);background:#fff;position:relative}
.abs{position:absolute}
.grad{background:linear-gradient(135deg,var(--red),var(--orange))}

/* header */
.topbar{position:absolute;top:0;left:0;width:1200px;height:78px;background:#fff}
.brand{position:absolute;left:142px;top:20px;display:flex;align-items:center;gap:8px;font-weight:900;font-size:30px;color:var(--red);letter-spacing:-.5px}
.brand-dot{width:14px;height:14px;background:var(--orange);border-radius:50%}
.contact-item{position:absolute;top:18px;display:flex;gap:12px;align-items:flex-start}
.contact-item small{display:block;font-size:13px;font-weight:500;color:var(--ink)}
.contact-item strong{display:block;font-size:19px;font-weight:500;color:var(--red);margin-top:2px}
.navbar{position:absolute;top:78px;left:0;width:1200px;height:47px;background:var(--nav)}
.navbar a{position:absolute;top:0;height:47px;line-height:47px;font-size:15px;font-weight:500;color:var(--ink);text-decoration:none}
.navbar a.active{background:var(--orange);color:#fff;padding:0 13px;color:#7a1a00}

/* hero */
.hero{position:absolute;top:125px;left:0;width:1200px;height:589px;background:var(--cream);overflow:hidden}
.hero-shape{position:absolute;left:0;top:0}
.pill{position:absolute;background:rgba(255,255,255,.22);color:#fff;font-weight:700;border-radius:6px}
.hero .pill{left:142px;top:111px;height:30px;padding:0 20px;line-height:30px;font-size:18px}
.hero h1{position:absolute;left:142px;top:153px;width:480px;font-size:46px;line-height:56px;font-weight:700;color:#fff}
.hero .sub{position:absolute;left:142px;top:336px;font-size:23px;line-height:31px;font-weight:500;color:#fff}
.btn{position:absolute;display:flex;align-items:center;justify-content:center;font-size:14px;font-weight:500;border-radius:7px;text-decoration:none}
.btn-white{background:#fff;color:var(--red)}
.btn-outline{border:2px solid #fff;color:#fff}
.video-frame{position:absolute;left:637px;top:97px;width:426px;height:395px;border:7px solid #fff;border-radius:26px;overflow:hidden;box-shadow:0 6px 20px rgba(0,0,0,.08)}
.photo{width:100%;height:100%}
.play{position:absolute;border-radius:50%;background:var(--red);display:flex;align-items:center;justify-content:center}

/* steps */
.section-title{position:absolute;left:0;width:1200px;text-align:center;font-weight:500;font-size:46px;color:var(--ink)}
.step{position:absolute;top:919px;width:221px;height:254px;border:4px solid var(--line);border-radius:18px;background:#fff;text-align:center}
.step .tag{position:absolute;top:-17px;left:50%;transform:translateX(-50%);background:var(--red);color:#fff;font-size:13px;font-weight:500;padding:6px 16px;border-radius:16px;border:3px solid #f5c8c8;white-space:nowrap}
.step svg{position:absolute;left:72px;top:36px}
.step h3{position:absolute;top:126px;left:0;width:100%;font-size:20px;line-height:24px;font-weight:500}
.step p{position:absolute;top:182px;left:10px;right:10px;font-size:14px;line-height:24px;color:var(--grey)}
.step.single h3{top:126px}

/* benefits */
.benefit-circle{position:absolute;left:144px;top:1319px;width:390px;height:390px;border-radius:50%;background:linear-gradient(160deg,var(--orange),var(--red))}
.machine{position:absolute;background:linear-gradient(90deg,#2b2b2b,#4a4a4a 45%,#bfbfbf 70%,#3a3a3a);border-radius:10px}
.benefits h2{position:absolute;left:598px;top:1270px;font-size:46px;font-weight:500}
.benefit{position:absolute;left:598px;height:70px;width:520px}
.benefit b{position:absolute;left:0;top:0;font-size:37px;font-weight:500;color:var(--red)}
.benefit h4{position:absolute;left:90px;top:0;font-size:18px;font-weight:500}
.benefit p{position:absolute;left:90px;top:30px;font-size:14px;color:var(--grey)}

/* audience */
.audience{position:absolute;top:1834px;left:0;width:1200px;height:729px;background:linear-gradient(180deg,#f6ede6,#fbf3ee 50%,#f6ebe3)}
.aud-card{position:absolute;top:193px;width:441px;height:351px;border-radius:22px;overflow:hidden}
.aud-caption{position:absolute;top:490px;width:363px;height:117px;background:#fff;border-radius:18px;text-align:center;box-shadow:0 6px 18px rgba(0,0,0,.06)}
.aud-caption h3{margin-top:18px;font-size:19px;font-weight:500}
.aud-caption p{margin:10px auto 0;width:300px;font-size:14px;line-height:23px;color:var(--grey)}
.arrow{position:absolute}

/* testimonials */
.quote{position:absolute;left:0;top:2736px;width:1200px;text-align:center;font-size:28px;font-weight:500;color:var(--red)}
.stars{position:absolute;left:0;top:2782px;width:1200px;text-align:center;color:#f7a400;font-size:17px;letter-spacing:3px}
.testimonial-text{position:absolute;left:200px;top:2815px;width:800px;text-align:center;font-style:italic;font-size:14.5px;line-height:24px;color:var(--grey)}
.client-name{position:absolute;left:500px;top:2910px;width:200px;text-align:center;font-size:34px;font-weight:700;color:#333}

/* video + cta */
.cta-band{position:absolute;top:3314px;left:0;width:1200px;height:644px;background:linear-gradient(180deg,var(--red),var(--orange) 90%);overflow:hidden}
.video-box{position:absolute;left:144px;top:3054px;width:912px;height:431px;border-radius:22px;overflow:hidden;box-shadow:0 20px 40px rgba(0,0,0,.15)}
.video-box .caption{position:absolute;left:0;top:290px;width:100%;text-align:center;font-size:27px;font-weight:500;color:#fff}
.btn-red{background:var(--red);color:#fff;border:2px solid #fff}
.cta-band h2{position:absolute;left:142px;top:300px;font-size:46px;line-height:55px;font-weight:700;color:#fff}
.cta-band .sub{position:absolute;left:142px;top:422px;font-size:25px;line-height:32px;font-weight:500;color:#fff}

/* footer */
.footer{position:absolute;top:3958px;left:0;width:1200px;height:409px;background:var(--dark);color:#fff}
.footer h5{position:absolute;top:78px;font-size:19px;font-weight:500}
.field{position:absolute;left:142px;top:117px;width:255px;height:49px;border:2px solid #fff;border-radius:25px;display:flex;align-items:center;gap:10px;padding-left:24px;font-size:14px}
.subscribe{position:absolute;left:142px;top:178px;width:255px;height:49px;border-radius:25px;background:var(--red);font-size:14px;font-weight:500;display:flex;align-items:center;justify-content:center}
.links{position:absolute;top:122px;list-style:none;font-size:14px;line-height:22.4px}
.links li::before{content:"»";margin-right:12px}
.touch{position:absolute;left:866px;font-size:14px;font-weight:500;display:flex;gap:10px;align-items:center}
.social{position:absolute;top:196px;width:38px;height:38px;border-radius:50%}
.divider{position:absolute;left:142px;top:296px;width:916px;height:1px;background:#444}
.copy{position:absolute;left:0;top:333px;width:1200px;text-align:center;font-size:14px}
</style>
</head>
<body>

<header class="topbar">
  <div class="brand">KelvaTrix482<span class="brand-dot"></span></div>
  <div class="contact-item" style="left:506px">
    <svg width="36" height="36" viewBox="0 0 24 24"><path fill="var(--red)" d="M6.6 10.8a15 15 0 0 0 6.6 6.6l2.2-2.2c.3-.3.7-.4 1-.2 1.1.4 2.3.6 3.6.6.6 0 1 .4 1 1V20c0 .6-.4 1-1 1A17 17 0 0 1 3 4c0-.6.4-1 1-1h3.5c.6 0 1 .4 1 1 0 1.3.2 2.5.6 3.6.1.3 0 .7-.2 1z"/></svg>
    <div><small>Call Us Today:</small><strong>+1 888 888 8888</strong></div>
  </div>
  <div class="contact-item" style="left:754px">
    <svg width="42" height="32" viewBox="0 0 42 32"><rect x="1" y="2" width="40" height="28" fill="var(--red)"/><path d="M2 3l19 15L40 3" stroke="#fff" stroke-width="2.5" fill="none"/></svg>
    <div><small>Mail Us Today:</small><strong>info@companyname.com</strong></div>
  </div>
</header>

<nav class="navbar">
  <a class="active" style="left:176px">Home</a>
  <a style="left:259px">Product</a>
  <a style="left:342px">Solutions</a>
  <a style="left:437px">ROI / Economics</a>
  <a style="left:581px">Case Studies</a>
  <a style="left:702px">Pricing</a>
  <a style="left:780px">About</a>
  <a style="left:851px">Resources</a>
  <a style="left:954px">Contact</a>
</nav>

<section class="hero">
  <svg class="hero-shape" width="1200" height="589">
    <defs><linearGradient id="heroGrad" x1="0" y1="0" x2="1" y2="1"><stop offset="0" stop-color="#f31c2a"/><stop offset="1" stop-color="#ff6a3d"/></linearGradient></defs>
    <path d="M0 0H790L668 470Q640 589 530 589H0Z" fill="url(#heroGrad)"/>
  </svg>
  <div class="pill">Meet Pindle</div>
  <h1>Your New Robotic Chef for High-Volume, Consistent Cooking</h1>
  <p class="sub">Increase throughput. Reduce labor.<br>Deliver perfect food every time.</p>
  <a class="btn btn-white" style="left:142px;top:412px;width:156px;height:46px">Request a Demo</a>
  <a class="btn btn-outline" style="left:307px;top:412px;width:152px;height:46px">Watch Pindle Cook</a>
  <div class="video-frame">
    <div class="photo" role="img" aria-label="Pindle cooking chamber stirring noodles, with ingredient dispensers on the left" style="background:radial-gradient(circle at 55% 55%,#6b5a44,#2e2e2e 55%,#9a9a9a 90%)"></div>
    <div class="play" style="left:172px;top:156px;width:68px;height:68px"><svg width="22" height="24"><path d="M3 2l17 10L3 22z" fill="#fff"/></svg></div>
  </div>
</section>

<h2 class="section-title" style="top:814px">How Pindle Works</h2>

<div class="step" style="left:142px">
  <span class="tag">STEP 1</span>
  <svg width="70" height="76" viewBox="0 0 70 76" fill="none" stroke="var(--red)" stroke-width="2.5"><path d="M6 34h58c0 16-12 26-29 26S6 50 6 34z"/><path d="M22 66h26"/><circle cx="20" cy="44" r="2"/><circle cx="30" cy="44" r="2"/><circle cx="40" cy="44" r="2"/><circle cx="50" cy="44" r="2"/><path d="M18 34c0-10 6-16 14-16M38 34c0-12 8-20 18-22M46 8l8 10"/></svg>
  <h3>Load<br>Ingredients</h3>
  <p>Smart batching sensors recognize load weight.</p>
</div>
<div class="step" style="left:375px">
  <span class="tag">STEP 2</span>
  <svg width="70" height="76" viewBox="0 0 70 76" fill="none" stroke="var(--red)" stroke-width="2.5"><rect x="20" y="8" width="38" height="56" rx="3"/><rect x="30" y="4" width="18" height="8" rx="2"/><path d="M28 24h22M28 32h22M28 40h16"/><path d="M8 44h14v20H8zM12 44v-6h6v6"/></svg>
  <h3>Select<br>Recipe</h3>
  <p>One-touch programming with automated settings.</p>
</div>
<div class="step" style="left:607px">
  <span class="tag">STEP 3</span>
  <svg width="70" height="76" viewBox="0 0 70 76" fill="none" stroke="var(--red)" stroke-width="2.5"><rect x="8" y="6" width="54" height="64" rx="4"/><path d="M8 22h54"/><circle cx="18" cy="14" r="2"/><circle cx="28" cy="14" r="2"/><circle cx="38" cy="14" r="2"/><circle cx="48" cy="14" r="2"/><rect x="16" y="32" width="38" height="28" rx="2"/><path d="M16 42h38"/></svg>
  <h3>Pindle<br>Cooks</h3>
  <p>Automated stirring, temperature control, and</p>
</div>
<div class="step" style="left:838px">
  <span class="tag">STEP 4</span>
  <svg width="70" height="76" viewBox="0 0 70 76" fill="none" stroke="var(--red)" stroke-width="2.5"><circle cx="35" cy="12" r="4"/><path d="M8 44a27 27 0 0 1 54 0z"/><path d="M4 48h62"/><path d="M22 56h26l-6 10H28z"/></svg>
  <h3 style="top:136px">Serve</h3>
  <p>Perfectly cooked food with zero inconsistency.</p>
</div>

<section class="benefits">
  <div class="benefit-circle"></div>
  <div class="machine" role="img" aria-label="Pindle cooking robot unit with touchscreen, cooking chamber and wheeled base" style="left:210px;top:1305px;width:251px;height:421px"></div>
  <h2>Key Benefits</h2>
  <div class="benefit" style="top:1350px"><b>15k+</b><h4>Labor savings</h4><p>Lorem ipsum dolor sit amet, consectetur adipiscing</p></div>
  <div class="benefit" style="top:1430px"><b>0%</b><h4>Zero inconsistency</h4><p>Lorem ipsum dolor sit amet, consectetur adipiscing</p></div>
  <div class="benefit" style="top:1510px"><b>24/7</b><h4>24/7 uptime</h4><p>Lorem ipsum dolor sit amet, consectetur adipiscing</p></div>
  <div class="benefit" style="top:1590px"><b>50%</b><h4>Throughput increases</h4><p>Lorem ipsum dolor sit amet, consectetur adipiscing</p></div>
  <div class="benefit" style="top:1670px"><b>20+</b><h4>Health &amp; safety compliance</h4><p>Lorem ipsum dolor sit amet, consectetur adipiscing</p></div>
</section>

<section class="audience" role="img" aria-label="Soft-focus restaurant dining room background">
  <h2 class="section-title" style="top:112px">Who It’s For</h2>
  <svg class="arrow" style="left:52px;top:350px" width="40" height="28"><path d="M38 14H4M16 2L4 14l12 12" stroke="#111" stroke-width="2.5" fill="none"/></svg>
  <svg class="arrow" style="left:1108px;top:350px" width="40" height="28"><path d="M2 14h34M24 2l12 12-12 12" stroke="#111" stroke-width="2.5" fill="none"/></svg>
  <div class="aud-card" style="left:144px" role="img" aria-label="Kitchen utensils, plates and a chef hat on a counter" ><div class="photo" style="background:linear-gradient(160deg,#4a3a2e,#8d6a4c 55%,#d9d2c8)"></div></div>
  <div class="aud-card" style="left:615px" role="img" aria-label="Bowl of spaghetti with tomatoes, basil, olive oil and cheese"><div class="photo" style="background:linear-gradient(160deg,#3a2e26,#b4512b 55%,#e6d6bf)"></div></div>
  <div class="aud-caption" style="left:183px"><h3>QSR Restaurants</h3><p>Reduce labor reliance, handle rush hours effortlessly.</p></div>
  <div class="aud-caption" style="left:654px"><h3>Fast Casual</h3><p>Consistent prep for bowls, proteins, sauces.</p></div>
</section>

<h2 class="section-title" style="top:2651px">Testimonials</h2>
<p class="quote">Pindle helped us reduce cooking times by 40%.</p>
<div class="stars">★★★★★</div>
<p class="testimonial-text">Lorem ipsum dolor sit amet, consectetur adipiscing elit, sed do eiusmod tempor incididunt ut labore et dolore magna aliqua. Ut enim ad minim veniam, quis nostrud exercitation ullamco laboris nisi ut aliquip ex ea commodo consequat. Duis aute irure dolor in reprehenderit in voluptate velit esse cillum dolore eu fugiat nulla pariatur.</p>
<svg class="arrow" style="left:428px;top:2917px" width="48" height="28"><circle cx="16" cy="14" r="13" fill="var(--orange)"/><path d="M46 14H4M14 4L4 14l10 10" stroke="#111" stroke-width="3" fill="none"/></svg>
<div class="client-name">Sproutly</div>
<svg class="arrow" style="left:724px;top:2917px" width="48" height="28"><circle cx="32" cy="14" r="13" fill="var(--orange)"/><path d="M2 14h42M34 4l10 10-10 10" stroke="#111" stroke-width="3" fill="none"/></svg>

<section class="cta-band">
  <svg class="abs" style="left:0;top:0" width="1200" height="644"><path d="M576 644Q760 470 1200 456V644Z" fill="#fff"/></svg>
  <h2>Ready to See Pindle<br>in Action?</h2>
  <p class="sub">Boost efficiency, eliminate inconsistency,<br>and scale your kitchen.</p>
  <a class="btn btn-outline" style="left:142px;top:505px;width:155px;height:47px">Book a Demo</a>
  <div class="machine" role="img" aria-label="Pindle cooking robot unit on wheels" style="left:817px;top:266px;width:259px;height:420px"></div>
</section>

<div class="video-box">
  <div class="photo" role="img" aria-label="Trade show booth with staff demonstrating the cooking robot" style="background:linear-gradient(120deg,#3b4450,#1f3a6e 50%,#5a5a5a)"></div>
  <div class="play" style="left:422px;top:178px;width:68px;height:68px"><svg width="22" height="24"><path d="M3 2l17 10L3 22z" fill="#fff"/></svg></div>
  <p class="caption">Watch Pindle cook a full batch from start to finish.</p>
  <a class="btn btn-red" style="left:380px;top:341px;width:152px;height:46px">See More Videos</a>
</div>

<footer class="footer">
  <h5 style="left:142px">Newsletter</h5>
  <div class="field"><svg width="16" height="12"><rect width="16" height="12" rx="1" fill="#fff"/><path d="M1 1l7 6 7-6" stroke="#262626" stroke-width="1.5" fill="none"/></svg>Email address</div>
  <div class="subscribe">SUBSCRIBE</div>
  <h5 style="left:470px">Quick Links</h5>
  <ul class="links" style="left:470px"><li>Home</li><li>Our Story</li><li>Products</li><li>Resources</li><li>Blog</li><li>Contact</li></ul>
  <h5 style="left:654px">Support</h5>
  <ul class="links" style="left:654px"><li>Get Involved</li><li>Support</li><li>Terms of Service</li><li>FAQ</li><li>Blog</li><li>Contact</li></ul>
  <h5 style="left:866px">Get in Touch</h5>
  <div class="touch" style="top:122px"><svg width="14" height="14" viewBox="0 0 24 24"><path fill="var(--red)" d="M6.6 10.8a15 15 0 0 0 6.6 6.6l2.2-2.2c.3-.3.7-.4 1-.2 1.1.4 2.3.6 3.6.6.6 0 1 .4 1 1V20c0 .6-.4 1-1 1A17 17 0 0 1 3 4c0-.6.4-1 1-1h3.5c.6 0 1 .4 1 1 0 1.3.2 2.5.6 3.6z"/></svg>+1 888 888 8888</div>
  <div class="touch" style="top:148px"><svg width="14" height="11"><rect width="14" height="11" fill="var(--red)"/></svg>info@companyname.com</div>
  <span class="social" style="left:867px;background:#fff"></span>
  <span class="social" style="left:915px;background:var(--red)"></span>
  <div class="divider"></div>
  <p class="copy">© Copyrights 2025 | All Rights Reserved</p>
</footer>

</body>
</html>
```